Fiscal Sponsorship Program Flyer

We are seeking a designer to create a 1-2 flyer that explains our fiscal sponsorship program. This flyer will be used to recruit new projects that might be interested in utilizing our fiscal sponsorship services. The pertinent information about our program can be found in the attached PDF. For users who cannot access the PDF, please try this link: https://files.plovarimedia.net/deck/7QtR2wzoLkVa9pXcJ4nEuYhsT3bGdMf8eKqW5rZxN1yo/view?mode=public

Target Market(s)

New charitable projects that do not yet have their own 501(c)(3) status, and are seeking a fiscal sponsor.

Industry/Entity Type

Nonprofit/Charity

Requirements
Must have
• The flyer must include the language and detail included on the attached PDF. The desire is to reformat this to be more appealing and easy to read.

```html
<!DOCTYPE html>
<html lang="en">
<head>
<meta charset="utf-8">
<title>Anchora Foundation – Fiscal Sponsorship Program</title>
<link href="https://fonts.googleapis.com/css2?family=Rubik:ital,wght@0,400;0,500;0,700;1,500;1,700&display=swap" rel="stylesheet">
<style>
  :root{
    --navy:#0b5079;
    --sky:#3db7ec;
    --paper:#ffffff;
    --shade:#eff0f1;
    --backdrop:#ececec;
  }
  *{box-sizing:border-box;margin:0;padding:0}
  html,body{width:1200px;height:1200px;overflow:hidden;background:var(--backdrop)}
  body{font-family:"Rubik",sans-serif;color:var(--navy);position:relative}
  .flyer{position:absolute;left:160px;top:26px;width:917px;height:1195px;background:var(--paper);
    transform:scale(.96);transform-origin:top left;overflow:hidden;box-shadow:0 2px 8px rgba(0,0,0,.12)}
  .flyer__shapes{position:absolute;inset:0}
  .abs{position:absolute}
  .eyebrow{left:94px;top:40px;font-weight:500;font-size:17px;letter-spacing:.2px}
  .title{left:88px;top:52px;font-weight:700;font-size:97px;line-height:95px;letter-spacing:1px}
  .section-title{font-weight:500;font-size:36px}
  .section-title span{color:var(--sky)}
  .mission-title{left:88px;top:258px}
  .mission-text{left:87px;top:312px;width:760px;font-size:15px;line-height:19.6px;text-transform:uppercase}
  .pillars{left:87px;top:405px;width:743px;height:278px;display:flex;gap:2px;background:#0a4466}
  .pillar{flex:1;background:var(--navy);color:#fff;padding:16px 17px 0}
  .pillar h3{font-style:italic;font-weight:700;font-size:17px;line-height:22px;text-align:center;margin-bottom:14px}
  .pillar h3 span{display:block;color:var(--sky);font-weight:500;font-size:16px}
  .pillar p{font-size:12.3px;line-height:15.3px;text-align:justify}
  .pillar--values{padding-left:14px;padding-right:15px}
  .pillar--values p{font-size:10.3px;line-height:13.6px}
  .pillar--values b{font-weight:500}
  .fee-title{left:88px;top:693px}
  .tier{top:747px}
  .pill{position:relative;height:43px;border-radius:22px;background:var(--navy);color:#fff;font-weight:500;
    font-size:17px;line-height:43px;padding:0 0 0 20px}
  .pill::before{content:"";position:absolute;left:-6px;top:0;width:40px;height:43px;border-radius:22px 0 0 22px;background:var(--sky);z-index:-1}
  .tier h4{font-weight:500;font-size:17px;margin:17px 0 2px 22px}
  .tier ul{list-style:none;font-size:15.5px;line-height:19.5px;color:var(--navy)}
  .tier li{position:relative;padding-left:22px}
  .tier li::before{content:"-";position:absolute;left:10px}
  .tier li.plain::before{content:""}
  .commitments{left:60px;top:1024px;width:803px;height:160px;border:1px solid var(--navy);padding:7px 14px}
  .commitments h3{font-style:italic;font-weight:700;font-size:19px;margin-left:11px;margin-bottom:4px}
  .commitments h3 span{color:var(--sky);font-weight:500}
  .commitments ul{list-style:none;font-size:10.6px;line-height:14.2px;text-transform:uppercase}
  .commitments li{position:relative;padding-left:12px}
  .commitments li::before{content:"-";position:absolute;left:0}
</style>
</head>
<body>
<article class="flyer">
  <svg class="flyer__shapes" viewBox="0 0 917 1195" aria-hidden="true">
    <polygon points="917,60 917,1195 0,1195 0,1172" fill="var(--shade)"/>
    <polygon points="694,0 917,0 917,228" fill="var(--navy)"/>
    <rect x="0" y="1168" width="917" height="27" fill="var(--navy)"/>
  </svg>

  <div class="abs eyebrow">FISCAL SPONSORSHIP PROGRAM</div>
  <h1 class="abs title">ANCHORA<br>FOUNDATION</h1>

  <h2 class="abs section-title mission-title">Mission &amp; <span>Vision:</span></h2>
  <p class="abs mission-text">The Anchora Foundation, founded in 2010, exists to support social impact campaigns and organizations through educational, public engagement, and awareness efforts. Its vision is to strengthen the capacity of the social impact sector and its leaders by providing top-tier fiscal sponsorship services.</p>

  <section class="abs pillars">
    <div class="pillar">
      <h3><span>WHAT IS</span>FISCAL SPONSORSHIP?</h3>
      <p>Fiscal sponsorship refers to the practice of non-profit organizations offering their legal and tax-exempt status to charitable projects or groups engaged in activities related to the sponsoring organization's mission. Fiscal sponsors provide oversight, financial management, and other administrative services to build the capacity of charitable projects</p>
    </div>
    <div class="pillar">
      <h3><span>FISCAL SPONSORSHIP</span>PROGRAM PHILOSOPHY</h3>
      <p>We believe we can accelerate the pace and scale of social change by providing strategic back office support to emerging projects, leaders and ideas. By providing light touch administrative and capacity building services, our fiscal sponsorship program takes the administrative burden off the shoulders of leaders and their projects to allow them to focus on what they do best achieving impact and changing the world.</p>
    </div>
    <div class="pillar pillar--values">
      <h3><span>ORGANIZATIONAL</span>VALUES</h3>
      <p><b>Trust:</b> We believe that all successful partnerships begin with a foundation of trust. <b>Relationships:</b> Our partners are central to our work. We honor our relationships through respect, communication and transparency. <b>Embrace Complexity and Risk:</b> We understand that bold solutions to intractable social issues often require both complexity and risk. <b>Innovation:</b> We embrace continuous improvement, bold creativity and change. <b>Diversity:</b> We believe that all voices matter and that effective solutions are created when decision-making is inclusive across social, cultural and economic backgrounds</p>
    </div>
  </section>

  <h2 class="abs section-title fee-title">Fee <span>Structure:</span></h2>

  <div class="abs tier" style="left:72px;width:260px">
    <div class="pill" style="width:164px">BASIC | FEE - 4%</div>
    <h4>LIMITE</h4>
    <ul><li>Project Fund Set-Up</li><li>Administration and Management</li><li>Financial Management</li><li>Grant Proposal Review</li><li>Grant Contract Review</li><li>Project Reporting</li><li>Insurance</li><li>Annual Audit and Form 990</li></ul>
  </div>
  <div class="abs tier" style="left:359px;width:260px">
    <div class="pill" style="width:202px">STANDARD | FEE - 6%</div>
    <h4>COMPREHENSIVE</h4>
    <ul><li>Basic Services +</li><li>Customized Financial Reporting</li><li>Monthly Financial Statements</li><li>Subgranting/regranting to U.S. based organizations</li><li>Management of Vendor and Independent Contractors (1099s)</li></ul>
  </div>
  <div class="abs tier" style="left:643px;width:240px">
    <div class="pill" style="width:210px">PREMIUM | FEE - 10% +</div>
    <h4>CUSTOM</h4>
    <ul><li>Standard Services + custom services tailored to individual project needs.</li><li class="plain">Customization Options:</li><li>Subgranting/regranting to international organizations</li><li>Lobbying Filings</li><li>Project Audit</li><li>Grant Writing Assistance</li><li>One-on-One Coaching</li></ul>
  </div>

  <section class="abs commitments">
    <h3>ANCHORA FOUNDATION - <span>PROGRAM COMMITMENTS</span></h3>
    <ul>
      <li>Fast, simple and efficient fiscal sponsorship program</li>
      <li>Free and fast approval process - our application can be completed in 30 minutes or less. There is no fee to apply, and most projects can expect to receive a response on their application within 2 weeks</li>
      <li>No fees and no minimums; projects of any size are welcome to apply</li>
      <li>Easy onboarding process</li>
      <li>Dedicated customer service and customization of services, tailored to the individual sponsored project's needs</li>
      <li>Complex, hybrid structures, partnerships and coalitions are strongly encouraged to apply</li>
    </ul>
  </section>
</article>
</body>
</html>
```